Local fast-growing company in the service sector

We are looking for a modern business card design, which should also appear on our letterheads

Target Market(s)

Private and industrial sectors

Contact Information for Business Card

Vorname Name
Lindkofer Str. 18
71468 Brennwald
Tel.: 07163-418259-0
Name@kovaltec-pbz.de

Colors
9d9d9d
919191
aaaaaa

Requirements
Must have
• The logo (file) in silver

```html
<!DOCTYPE html>
<html lang="en">
<head>
<meta charset="utf-8">
<title>KPBZ Stationery</title>
<link rel="stylesheet" href="https://fonts.googleapis.com/css2?family=Open+Sans:wght@400;600&family=Michroma&display=swap">
<style>
  :root {
    --backdrop: #e6e6e6;
    --paper: #ffffff;
    --ink: #141414;
    --body-text: #333333;
    --silver: #9d9d9d;
    --silver-mid: #919191;
    --silver-light: #aaaaaa;
  }
  * { margin: 0; padding: 0; box-sizing: border-box; }
  html, body { width: 1200px; height: 801px; overflow: hidden; }
  body {
    position: relative;
    background: var(--backdrop);
    font-family: "Open Sans", Arial, sans-serif;
  }

  .brand { display: flex; align-items: center; gap: 6px; }
  .brand-mark { background: var(--silver); flex: none; }
  .brand-name {
    font-family: "Michroma", Arial, sans-serif;
    color: var(--silver-light);
    line-height: 1;
  }
  .brand-domain {
    font-family: "Michroma", Arial, sans-serif;
    color: var(--silver-mid);
    line-height: 1;
    margin-top: 3px;
  }

  /* Letterhead */
  .letterhead {
    position: absolute; left: 90px; top: 21px;
    width: 485px; height: 629px;
    background: var(--paper);
  }
  .letterhead-header {
    position: absolute; right: 0; top: 0;
    width: 142px; height: 87px;
    background: var(--ink);
    display: flex; align-items: center; justify-content: center;
  }
  .letterhead-header .brand-mark { width: 12px; height: 12px; }
  .letterhead-header .brand-name { font-size: 17px; }
  .letterhead-header .brand-domain { font-size: 4.5px; }
  .letter-body {
    position: absolute; left: 28px; top: 177px; width: 430px;
    font-size: 9.4px; line-height: 14px; color: var(--body-text);
  }
  .letter-body p { margin-bottom: 10px; }
  .letterhead-footer {
    position: absolute; left: 4px; bottom: 10px;
    display: flex; gap: 10px; align-items: stretch;
  }
  .footer-bar { width: 14px; background: var(--ink); }
  .footer-address {
    font-style: normal; font-size: 7.5px; line-height: 10px; color: var(--body-text);
  }

  /* Folder */
  .folder {
    position: absolute; left: 600px; top: 60px;
    width: 507px; height: 698px;
  }
  .folder-cover { position: absolute; inset: 0; }
  .folder .brand {
    position: absolute; left: 130px; top: 163px; gap: 10px;
  }
  .folder .brand-mark { width: 38px; height: 38px; }
  .folder .brand-name { font-size: 50px; }
  .folder .brand-domain { font-size: 14px; margin-top: 5px; }
  .folder-url {
    position: absolute; left: 0; right: 0; bottom: 34px;
    text-align: center; font-size: 10px; font-weight: 600;
    letter-spacing: 3px; color: var(--ink);
  }

  /* Business cards */
  .card {
    position: absolute; top: 667px;
    width: 192px; height: 112px;
    background: var(--ink);
  }
  .card-front { left: 123px; }
  .card-back { left: 342px; }
  .card-front .brand { position: absolute; left: 50px; top: 10px; }
  .card .brand-mark { width: 11px; height: 11px; }
  .card .brand-name { font-size: 16px; }
  .card .brand-domain { font-size: 4.3px; }
  .card-contact {
    position: absolute; right: 26px; top: 58px;
    text-align: right; font-size: 5.6px; line-height: 7.4px; color: var(--silver-light);
  }
  .card-contact .contact-name { font-weight: 600; color: #ffffff; }
  .card-strip {
    position: absolute; left: 0; right: 0; bottom: 9px; height: 9px;
    background: linear-gradient(90deg, #cfcfcf, #8a8a8a 60%, #d8d8d8);
  }
  .card-back .brand {
    position: absolute; left: 0; right: 0; top: 30px; justify-content: center; gap: 8px;
  }
  .card-back .brand-mark { width: 14px; height: 14px; }
  .card .brand-name.large { font-size: 24px; }
  .card-back .brand-domain { font-size: 5.5px; }
  .card-url {
    position: absolute; left: 0; right: 0; bottom: 9px;
    text-align: center; font-size: 4.6px; letter-spacing: 1.5px; color: var(--silver);
  }
</style>
</head>
<body>

  <section class="letterhead">
    <header class="letterhead-header">
      <div class="brand">
        <span class="brand-mark"></span>
        <div>
          <div class="brand-name">KPBZ</div>
          <div class="brand-domain">kovaltec-pbz.de</div>
        </div>
      </div>
    </header>

    <div class="letter-body">
      <p>Dear [Recipient],</p>
      <p>We love the look of this stationery just the way it is. But you can add your own personal touch in almost no time.</p>
      <p>On the Design tab of the ribbon, check out the Themes, Colors, and Fonts galleries to preview different looks from a variety of choices. Then just click to apply the one you like.</p>
      <p>We’ve also created styles that let you match the formatting you see in this letter with just a click. On the Home tab of the ribbon, check out the Styles gallery for all styles used in this letter.</p>
      <p>Ready to add your digits? No problem. Just double-click the header area to add your contact information.</p>
      <p>Warm regards,<br>Jaren</p>
    </div>

    <footer class="letterhead-footer">
      <span class="footer-bar"></span>
      <address class="footer-address">
        Lindkofer Str. 18 &nbsp;71468 Brennwald<br>
        Tel.: 07163-418259-0<br>
        Name@kovaltec-pbz.de
      </address>
    </footer>
  </section>

  <section class="folder">
    <svg class="folder-cover" width="507" height="698" viewBox="0 0 507 698">
      <rect width="507" height="698" fill="var(--ink)"/>
      <polygon points="507,342 96,698 507,698" fill="var(--silver-light)"/>
      <polygon points="507,348 105,698 507,698" fill="var(--paper)"/>
    </svg>
    <div class="brand">
      <span class="brand-mark"></span>
      <div>
        <div class="brand-name">KPBZ</div>
        <div class="brand-domain">kovaltec-pbz.de</div>
      </div>
    </div>
    <div class="folder-url">www.yourbusiness.com</div>
  </section>

  <section class="card card-front">
    <div class="brand">
      <span class="brand-mark"></span>
      <div>
        <div class="brand-name">KPBZ</div>
        <div class="brand-domain">kovaltec-pbz.de</div>
      </div>
    </div>
    <div class="card-contact">
      <div class="contact-name">Your Name</div>
      <div>Your Title</div>
      <div>Lindkofer Str. 18 | 71468 Brennwald</div>
      <div>Tel.: 07163-418259-0</div>
      <div>Name@kovaltec-pbz.de</div>
    </div>
    <div class="card-strip"></div>
  </section>

  <section class="card card-back">
    <div class="brand">
      <span class="brand-mark"></span>
      <div>
        <div class="brand-name large">KPBZ</div>
        <div class="brand-domain">kovaltec-pbz.de</div>
      </div>
    </div>
    <div class="card-url">www.kovaltec-pbz.de</div>
  </section>

</body>
</html>
```